Pediatric Occupational Therapist Logo and Business Card Design

Business card for Pediatric Occupational Therapist. Would like something that is colorful and would catch people's eyes. Child friendly is needed. I have attached some ideas of things that i liked that were found online. The card will be placed in certain places where parents will be and the card / logo will have to catch their eye and make them think some of the following things 1) this person is a professional 2) this person seems very child friendly 3) i would like to hire this person to be my kids occupational therapist.

Target Market(s)

Moms who see the card and will make decisions to hire as a result

Industry/Entity Type

Business

Contact Information for Business Card

Would like the front to be on the simpler side with the back and expanded version of the front smaller logo.

Font styles to use
Sans Serif

Requirements
Must have
• Brenna Tulliver OTR/L
• brennatulliverot@examplemail.net

```html
<!DOCTYPE html>
<html lang="en">
<head>
<meta charset="utf-8">
<title>Brenna Tulliver OTR/L – Business Card</title>
<link href="https://fonts.googleapis.com/css2?family=Raleway:wght@400;500;700&family=Quicksand:wght@600;700&display=swap" rel="stylesheet">
<style>
  :root {
    --backdrop: #eeeeec;
    --card-yellow: #f2c53d;
    --card-yellow-deep: #e8b92a;
    --card-white: #ffffff;
    --ink: #4a4538;
    --ink-soft: #555555;
    --brand-yellow: #f2c12e;
    --chick-tone: #f4c430;
    --kids-pink: #e46ab0;
    --kids-green: #3aa34a;
    --shadow: rgba(0, 0, 0, 0.12);
  }
  * { box-sizing: border-box; margin: 0; padding: 0; }
  html, body {
    width: 1200px;
    height: 800px;
    overflow: hidden;
    background: var(--backdrop);
  }
  .canvas {
    position: relative;
    width: 1200px;
    height: 800px;
    display: flex;
    align-items: center;
    justify-content: center;
    gap: 50px;
  }
  .card {
    position: relative;
    width: 525px;
    height: 300px;
    box-shadow: 0 6px 18px var(--shadow);
  }

  /* Contact side */
  .card--contact {
    background: linear-gradient(160deg, var(--card-yellow) 0%, var(--card-yellow-deep) 100%);
    font-family: "Raleway", sans-serif;
    color: var(--ink);
  }
  .contact-block {
    position: absolute;
    left: 40px;
    bottom: 36px;
  }
  .contact-name {
    font-weight: 700;
    font-size: 19px;
    letter-spacing: 0.2px;
  }
  .contact-role {
    font-weight: 500;
    font-size: 15px;
    margin-top: 4px;
  }
  .contact-list {
    list-style: none;
    margin-top: 26px;
    font-size: 14px;
    font-weight: 500;
    line-height: 1.45;
  }
  .contact-label {
    display: inline-block;
    width: 54px;
  }

  /* Logo side */
  .card--logo {
    background: var(--card-white);
  }
  .mascot {
    position: absolute;
    left: 50%;
    top: 52px;
    width: 80px;
    height: 90px;
    transform: translateX(-50%);
    border-radius: 45% 45% 40% 40%;
    background: radial-gradient(circle at 55% 45%, var(--chick-tone) 0%, #f7d774 70%, #ffffff 100%);
  }
  .brand-name {
    position: absolute;
    left: 0;
    right: 0;
    top: 152px;
    text-align: center;
    font-family: "Quicksand", sans-serif;
    font-weight: 700;
    font-size: 34px;
    color: var(--brand-yellow);
    letter-spacing: 0.5px;
  }
  .brand-email {
    position: absolute;
    left: 0;
    right: 0;
    top: 196px;
    text-align: center;
    font-family: "Raleway", sans-serif;
    font-weight: 500;
    font-size: 15px;
    color: var(--ink-soft);
  }
  .kids-art {
    position: absolute;
    left: 38px;
    bottom: 18px;
    width: 92px;
    height: 74px;
    border-radius: 10px;
    background: linear-gradient(90deg, var(--kids-pink) 0%, #f2b5d6 50%, var(--kids-green) 100%);
    opacity: 0.75;
  }
</style>
</head>
<body>
  <main class="canvas">
    <section class="card card--contact" aria-label="Contact side">
      <div class="contact-block">
        <p class="contact-name">Brenna Tulliver</p>
        <p class="contact-role">Occupational Therapist</p>
        <ul class="contact-list">
          <li><span class="contact-label">Phone</span>: 000.000.0000</li>
          <li><span class="contact-label">Email</span>: brennatulliverot@examplemail.net</li>
        </ul>
      </div>
    </section>

    <section class="card card--logo" aria-label="Logo side">
      <div class="mascot" role="img" aria-label="Hand-drawn yellow chick mascot"></div>
      <p class="brand-name">Brenna Tulliver OTR/L</p>
      <p class="brand-email">brennatulliverot@examplemail.net</p>
      <div class="kids-art" role="img" aria-label="Hand-drawn doodle of two children holding hands, one in a pink dress and one in a green shirt"></div>
    </section>
  </main>
</body>
</html>
```